Tending Our Garden eBook Cover Design

I want to deisgn a cover for my eBook (FRONT COVER) and the title is:

What I Grew From a Single Spark. And Why It Matters
By KT Dorran

TITLE CHANGED TO: UNDER THE WILLOW TREE; WHERE I FOUND MY QUIET STRENGTH AND WHERE YOU MIGHT TOO

The color palette is attached. Along with some photos options of me. Along with the ebook in WORD Document. My website is www.KTDorranLive.example. You can use a different color palette if you think it is best

Target Market(s)

women who look to build a personal brand

Industry/Entity Type

health and wellness

Requirements
Must have
• the title
Nice to have
• use my picture on the cover; but that is optional
Should not have
• any men

```html
<!DOCTYPE html>
<html lang="en">
<head>
<meta charset="UTF-8">
<title>Under the Willow Tree – KT Dorran</title>
<link href="https://fonts.googleapis.com/css2?family=Bebas+Neue&family=Oswald:wght@600&display=swap" rel="stylesheet">
<style>
  :root {
    --paper: #ffffff;
    --teal: #55938f;
    --teal-deep: #37756f;
    --portrait-dark: #2b2b30;
    --portrait-mid: #3a3a40;
  }
  html, body {
    margin: 0;
    padding: 0;
    width: 718px;
    height: 1200px;
    overflow: hidden;
    background: var(--paper);
  }
  .cover {
    position: relative;
    width: 718px;
    height: 1200px;
    overflow: hidden;
    background: var(--paper);
  }
  .author-portrait {
    position: absolute;
    left: 340px;
    top: 60px;
    width: 378px;
    height: 1140px;
  }
  .title {
    position: absolute;
    left: 31px;
    top: 22px;
    margin: 0;
    font-family: "Bebas Neue", "Oswald", sans-serif;
    font-weight: 400;
    font-size: 187px;
    line-height: 167px;
    color: var(--teal);
    letter-spacing: 1px;
  }
  .title span { display: block; }
  .subtitle {
    position: absolute;
    left: 29px;
    top: 738px;
    margin: 0;
    font-family: "Bebas Neue", "Oswald", sans-serif;
    font-weight: 400;
    font-size: 72px;
    line-height: 68px;
    color: var(--teal-deep);
  }
  .subtitle span { display: block; }
  .author-name {
    position: absolute;
    left: 31px;
    top: 1104px;
    margin: 0;
    font-family: "Oswald", sans-serif;
    font-weight: 600;
    font-size: 56px;
    line-height: 60px;
    color: var(--teal);
    letter-spacing: 1px;
  }
</style>
</head>
<body>
  <main class="cover">
    <svg class="author-portrait" role="img" aria-label="Photo of the smiling author in a black turtleneck with a long pendant necklace" viewBox="0 0 378 1140" preserveAspectRatio="none">
      <defs>
        <linearGradient id="portraitTone" x1="0" y1="0" x2="0" y2="1">
          <stop offset="0" stop-color="#3a3a40"/>
          <stop offset="1" stop-color="#2b2b30"/>
        </linearGradient>
      </defs>
      <path d="M220 10 C290 0 370 30 378 60 L378 1140 L90 1140 L70 860 L50 650 L40 420 C60 380 120 360 170 330 L190 280 C170 230 170 80 220 10 Z" fill="url(#portraitTone)"/>
    </svg>

    <h1 class="title">
      <span>Under</span>
      <span>The</span>
      <span>Willow</span>
      <span>Tree;</span>
    </h1>

    <p class="subtitle">
      <span>Where I Found My</span>
      <span>Quiet Strength</span>
      <span>And Where You</span>
      <span>Might Too</span>
    </p>

    <p class="author-name">KT DORRAN</p>
  </main>
</body>
</html>
```